Harvest Lantern Ministry Conference

I am in need of promotional graphics for our upcoming event. This event, titled "Harbor Crest Youth Conference", is a weekend event for teenagers 11-19 years old. They hear from religious speakers, listen to a band, and do other fun activities. Graphic design should be geared to young adults/older teens. Alcohol, drugs, smoking are not permitted. Open to any color combinations you think fit with your design.
Event Info:
November 1-3, 2024
Tellwood Exhibit Hall, Sioux Falls, SD
Speakers: Marcus Linden (man in light blue shirt in attached photo), Tessa Vandermeer (woman in attached photo), Colin Hardy ( man in dark colored shirt in attached photo)
Worship: KW Collective
HarborCrestGather.com
#742GR
Our Organization Logo (attached): Lumenward
Once designed, I need the following graphics file sizes:
-11x17 Vertical Poster design: include all event info AND a "blank" space on the bottom or box for groups to add their own details/information. Also include the QRV logo and our organization logo Lumenward in some way.
-Make an additional copy of the 11x17 pdf with cut and bleed lines for printing, please.
-4x3 horizontal postcard: include all event info on 1 side including Lumenward logo and QRV; blank backside
-Main Graphic Slide: formatted to fit a widescreen 16x9 screen. Include event name, hashtag, QRV and Lumenward logo
-social media graphic(s) for event: can incorporate some or all of the event details. WILLING TO ADJUST BUDGET FOR SOCIAL MEDIA graphics.
-4.25in x 2.75in vertical badge: include event title on front with Lumenward logo
Target Market
ages 11-19
Target Market(s)
11-19 years old
Industry/Entity Type
Christian Youth Ministry

```html
<!DOCTYPE html>
<html lang="en">
<head>
<meta charset="utf-8">
<title>Harbor Crest Youth Conference – Poster</title>
<link rel="stylesheet" href="https://fonts.googleapis.com/css2?family=Anton&family=Archivo:wght@700;800&family=Great+Vibes&display=swap">
<style>
  :root {
    --backdrop: #807f80;
    --paper: #efefef;
    --blue: #1450a0;
    --sky: #0f75bc;
    --green: #0aa283;
    --orange: #e88d25;
    --red: #e41f26;
    --ink: #111111;
    --white: #ffffff;
  }
  * { margin: 0; padding: 0; box-sizing: border-box; }
  html, body { width: 1200px; height: 800px; overflow: hidden; }
  body {
    background: var(--backdrop);
    font-family: "Archivo", Arial, sans-serif;
    position: relative;
  }
  .poster {
    position: absolute;
    left: 367px; top: 40px;
    width: 466px; height: 720px;
    background: var(--paper);
    overflow: hidden;
  }
  .poster__shapes { position: absolute; inset: 0; width: 466px; height: 720px; }

  .org-mark {
    position: absolute; left: 56px; top: 134px;
    display: flex; align-items: center; gap: 5px;
    font-weight: 800; font-size: 13px; color: var(--sky);
  }
  .org-mark__dot { width: 10px; height: 10px; border-radius: 50%; background: var(--sky); }

  .title {
    position: absolute; left: 54px; top: 152px;
    font-family: "Anton", Impact, sans-serif;
    font-weight: 400; font-size: 104px; line-height: 94px;
    text-transform: uppercase; letter-spacing: -1px;
  }
  .title__line { display: block; }
  .title__line--blue { color: var(--blue); }
  .title__line--green { color: var(--green); }
  .title__line--orange { color: var(--orange); }

  .title__script {
    position: absolute; left: 44px; top: 372px;
    font-family: "Great Vibes", cursive;
    font-size: 94px; color: var(--sky);
    white-space: nowrap;
  }

  .speakers { position: absolute; left: 112px; top: 476px; width: 320px; }
  .speakers__label {
    font-size: 9px; font-weight: 800; color: var(--blue);
    letter-spacing: .3px; margin-bottom: 4px;
  }
  .speakers__row { display: flex; gap: 12px; align-items: flex-start; }
  .speaker { position: relative; width: 96px; height: 96px; flex: none; }
  .speaker:nth-child(2) { margin-top: -12px; }
  .speaker:nth-child(3) { margin-top: -24px; }
  .speaker__photo { width: 100%; height: 100%; }
  .speaker__photo--one { background: linear-gradient(160deg, #b9c9d8, #6f9cc0 55%, #2c2c34); }
  .speaker__photo--two { background: linear-gradient(160deg, #f1ece7, #d7b488 55%, #b58b5e); }
  .speaker__photo--three { background: linear-gradient(160deg, #6d5b44, #3b3a36 55%, #1d2330); }
  .speaker__name {
    position: absolute; left: 8px; bottom: -6px;
    padding: 4px 6px; font-size: 7.5px; font-weight: 800;
    color: var(--white); text-transform: uppercase; white-space: nowrap;
  }
  .speaker__name--blue { background: var(--blue); }
  .speaker__name--green { background: var(--green); }
  .speaker__name--orange { background: var(--orange); }

  .date-band {
    position: absolute; left: 140px; top: 632px;
    background: var(--red); color: var(--white);
    font-weight: 800; font-size: 22px; letter-spacing: .5px;
    padding: 4px 12px;
  }
  .details {
    position: absolute; left: 150px; top: 676px;
    font-size: 8.5px; font-weight: 800; color: var(--blue);
    line-height: 1.45; text-transform: uppercase;
  }
  .partner-mark {
    position: absolute; left: 380px; top: 590px;
    display: flex; align-items: center; gap: 4px;
    font-weight: 800; font-size: 22px; color: var(--ink);
  }
  .partner-mark__ring { width: 14px; height: 14px; border-radius: 50%; border: 2px solid var(--sky); }
</style>
</head>
<body>
  <main class="poster">
    <svg class="poster__shapes" viewBox="0 0 466 720" aria-hidden="true">
      <polygon points="380,18 420,18 412,50" fill="var(--red)"/>
      <polygon points="432,20 450,20 446,34" fill="var(--blue)"/>
      <polygon points="405,66 450,58 446,100" fill="var(--sky)"/>
      <polygon points="344,52 362,48 358,66" fill="var(--orange)"/>
      <polygon points="364,96 388,92 386,120" fill="var(--blue)"/>
      <polygon points="404,124 440,112 440,150" fill="var(--green)"/>
      <polygon points="0,0 26,0 10,26" fill="var(--green)"/>
      <polygon points="40,560 40,592 64,572" fill="var(--sky)"/>
      <polygon points="96,588 96,614 122,596" fill="var(--blue)"/>
      <polygon points="54,612 54,668 106,638" fill="var(--orange)"/>
      <polygon points="112,636 112,666 140,646" fill="var(--green)"/>
      <polygon points="58,672 58,700 84,684" fill="var(--blue)"/>
      <polygon points="86,672 86,720 140,720" fill="var(--blue)"/>
      <polygon points="128,690 128,718 154,704" fill="var(--red)"/>
    </svg>

    <div class="org-mark"><span class="org-mark__dot"></span>Lumenward</div>

    <h1 class="title">
      <span class="title__line title__line--blue">Harbor</span>
      <span class="title__line title__line--green">Crest</span>
      <span class="title__line title__line--orange">Youth</span>
    </h1>
    <div class="title__script">Conference</div>

    <section class="speakers">
      <p class="speakers__label">SPEAKERS -</p>
      <div class="speakers__row">
        <figure class="speaker">
          <div class="speaker__photo speaker__photo--one" role="img" aria-label="Portrait photo of speaker Marcus Linden in a light blue shirt"></div>
          <figcaption class="speaker__name speaker__name--blue">Marcus Linden</figcaption>
        </figure>
        <figure class="speaker">
          <div class="speaker__photo speaker__photo--two" role="img" aria-label="Portrait photo of speaker Tessa Vandermeer"></div>
          <figcaption class="speaker__name speaker__name--green">Tessa Vandermeer</figcaption>
        </figure>
        <figure class="speaker">
          <div class="speaker__photo speaker__photo--three" role="img" aria-label="Portrait photo of speaker Colin Hardy in a dark shirt"></div>
          <figcaption class="speaker__name speaker__name--orange">Colin Hardy</figcaption>
        </figure>
      </div>
    </section>

    <div class="partner-mark"><span class="partner-mark__ring"></span>QRV</div>

    <p class="date-band">NOVEMBER 1-3, 2024</p>
    <p class="details">Worship: KW Collective<br>HarborCrestGather.com &nbsp;#742GR</p>
  </main>
</body>
</html>
```